Insurance Pull Down Bar Ad

I need a simple magazine ad. At the top of the ad will read "Need Insurance? We Can Help." Below it will be a pull down bar that has been clicked on by a cursor. In the pull-down bar will be (one above the other) "medical, dental, life, disability, office-overhead, personal accident, travel, medical evacuation, critical illness and hospital indemnity."

In the attached file there is a logo in the upper left corner. It has our name and exclusively endorsed below it. Use this in the ad.

Colors should go with the logo attached.

We will need social media icons at the bottom: Facebook, Youtube, Twitter, LinkedIn

I need it in a file that a graphic artist can edit.

Insurance

```html
<!DOCTYPE html>
<html lang="en">
<head>
<meta charset="utf-8">
<title>Need Insurance? We Can Help</title>
<link href="https://fonts.googleapis.com/css2?family=Merriweather:wght@900&family=Libre+Caslon+Text:ital,wght@0,400;1,400&display=swap" rel="stylesheet">
<style>
  :root {
    --crimson: #a91e3c;
    --sky-top: #98adad;
    --sky-bottom: #dfe5e5;
    --row-light: #ffffff;
    --row-tint: #a6b8b8;
    --row-text-dark: #6a6f70;
    --row-text-light: #ffffff;
    --track: #e6eaea;
    --thumb: #e9eeee;
    --ink-grey: #5d6263;
    --footer-top: #ffffff;
    --footer-bottom: #e4e7e7;
    --icon: #8fa3a8;
  }
  * { margin: 0; padding: 0; box-sizing: border-box; }
  html, body { width: 907px; height: 1200px; overflow: hidden; background: #fff; }
  .ad {
    position: relative;
    width: 907px;
    height: 1200px;
    overflow: hidden;
    font-family: "Libre Caslon Text", Georgia, serif;
  }
  .ad__field {
    position: absolute; left: 0; top: 0; width: 907px; height: 889px;
    background: linear-gradient(180deg, var(--sky-top) 0%, #b4c3c3 40%, var(--sky-bottom) 100%);
  }
  .ad__banner { position: absolute; left: 0; top: 0; }
  .headline {
    position: absolute; left: 0; top: 84px; width: 907px;
    text-align: center; color: #fff;
    font-family: "Merriweather", Georgia, serif; font-weight: 900;
    font-size: 84px; line-height: 98px; letter-spacing: -0.5px;
  }
  .dropdown {
    position: absolute; left: 249px; top: 434px; width: 409px;
    list-style: none;
  }
  .dropdown__item {
    height: 34px; margin-bottom: 2.3px;
    display: flex; align-items: center; justify-content: center;
    font-variant: small-caps; font-size: 25px; letter-spacing: 1.5px;
    line-height: 1;
  }
  .dropdown__item:nth-child(odd) { background: var(--row-light); color: var(--row-text-dark); }
  .dropdown__item:nth-child(even) { background: var(--row-tint); color: var(--row-text-light); }
  .scrollbar {
    position: absolute; left: 677px; top: 434px; width: 29px; height: 360px;
    background: linear-gradient(180deg, #cfd7d7 0%, var(--track) 100%);
  }
  .scrollbar__upper {
    position: absolute; left: 0; top: 0; width: 29px; height: 133px;
    background: linear-gradient(180deg, #7e9a9a 0%, #b7c6c6 100%);
  }
  .scrollbar__thumb {
    position: absolute; left: 0; top: 134px; width: 29px; height: 84px;
    background: var(--thumb);
  }
  .cursor { position: absolute; left: 692px; top: 608px; }
  .ad__footer {
    position: absolute; left: 0; top: 889px; width: 907px; height: 311px;
    background: linear-gradient(180deg, var(--footer-top) 0%, var(--footer-top) 61%, #f4f5f5 62%, var(--footer-bottom) 100%);
  }
  .brand-name {
    position: absolute; left: 0; top: 946px; width: 907px;
    text-align: center; color: var(--crimson);
    font-size: 34px; line-height: 40px; letter-spacing: 0.5px;
  }
  .endorsement {
    position: absolute; left: 0; top: 1033px; width: 907px; text-align: center;
    font-style: italic; font-size: 15px; color: var(--ink-grey);
  }
  .social {
    position: absolute; left: 392px; top: 1114px;
    display: flex; gap: 9px; list-style: none;
  }
  .social__item { width: 25px; height: 25px; background: var(--icon); border-radius: 3px; }
</style>
</head>
<body>
<main class="ad">
  <div class="ad__field"></div>

  <svg class="ad__banner" width="907" height="339" viewBox="0 0 907 339" aria-hidden="true">
    <polygon points="0,0 907,0 850,339 60,339" fill="var(--crimson)"/>
  </svg>

  <h1 class="headline">Need Insurance?<br>We Can Help</h1>

  <ul class="dropdown">
    <li class="dropdown__item">Medical</li>
    <li class="dropdown__item">Dental</li>
    <li class="dropdown__item">Life</li>
    <li class="dropdown__item">Disability</li>
    <li class="dropdown__item">Office-overhead</li>
    <li class="dropdown__item">Personal accident</li>
    <li class="dropdown__item">Travel</li>
    <li class="dropdown__item">Medical evacuation</li>
    <li class="dropdown__item">Critical illness</li>
    <li class="dropdown__item">Hospital indemnity</li>
  </ul>

  <div class="scrollbar">
    <div class="scrollbar__upper"></div>
    <div class="scrollbar__thumb"></div>
  </div>

  <svg class="cursor" width="64" height="64" viewBox="0 0 64 64" aria-hidden="true">
    <polygon points="10,12 50,24 38,32 58,52 50,60 30,40 22,52" fill="#6f7b7d" opacity="0.45" transform="translate(3,3)"/>
    <polygon points="10,12 50,24 38,32 58,52 50,60 30,40 22,52" fill="#ffffff"/>
  </svg>

  <footer class="ad__footer"></footer>

  <p class="brand-name">Harborline Physician Cover</p>
  <p class="endorsement">Exclusively endorsed by the Harborline Medical Society</p>

  <ul class="social" aria-label="Social media">
    <li class="social__item"></li>
    <li class="social__item"></li>
    <li class="social__item"></li>
    <li class="social__item"></li>
  </ul>
</main>
</body>
</html>
```